Book Cover Design - Uncovering Weight Loss Secrets

I need a book cover design for a book called 'Folding The Map'. It is a book that goes through all of the secrets to weight loss, without any crazy shakes or workouts or pills or potions. The book is really focused on helping people understand that Weight loss is simple and has more to do with our mindset as well as the food we were eating. It is about taking personal responsibility not looking for the next fancy revolutionary product that is going to help them magically melt the fat away. The book is pragmatic in nature and breaks down in simple terms how we can lose weight and keep it off for the rest of our lives. It shows the user that it is simple to lose weight, but it takes effort. They should stop looking for a quick fix when it comes to weight loss but instead eat healthy for the rest of their lives.
The book is intended to be hard-hitting no holds barred approach. The book has the same title as my business name. I will attach the current logo that we use in the business. This doesn't need to be on the front of the book maybe at the back down the bottom somewhere.
I am looking to have both an e-book cover and a standard printed book cover.
I don't have any colours in mind, my logo can be adapted to be different colours or just white.
The message that I am wanting people to feel when they see my book, is that all these Weightloss fads are a joke, that I know the secrets that will get them to their weight loss goal even if they fail at everything else before.
On the cover it should say the following.
FOLDING THE MAP
Uncovering the Weight Loss Secrets
The big companies have been trying to keep hidden for years!
COLIN MAYHEW
People who have failed many times trying to lose weight & need help
Weight Loss

```html
<!DOCTYPE html>
<html lang="en">
<head>
<meta charset="UTF-8">
<title>Folding The Map — Colin Mayhew</title>
<link rel="stylesheet" href="https://fonts.googleapis.com/css2?family=Barlow+Condensed:wght@600;700&family=Barlow+Semi+Condensed:wght@700&display=swap">
<style>
  :root {
    --page-bg: #ffffff;
    --navy-core: #173d7a;
    --navy-mid: #0f2a5a;
    --navy-edge: #0a1733;
    --accent: #e6fb14;
    --white: #ffffff;
    --plate-well: #9aaabd;
    --plate-light: #7f94ad;
    --plate-mid: #5e7795;
    --plate-rim: #465f80;
    --plate-shadow: rgba(4, 12, 30, 0.55);
  }
  * { margin: 0; padding: 0; box-sizing: border-box; }
  html, body {
    width: 1200px;
    height: 1200px;
    overflow: hidden;
    background: var(--page-bg);
  }
  .cover {
    position: absolute;
    left: 226px;
    top: 40px;
    width: 748px;
    height: 1120px;
    overflow: hidden;
    background: radial-gradient(ellipse 70% 55% at 50% 32%, var(--navy-core) 0%, var(--navy-mid) 55%, var(--navy-edge) 100%);
    font-family: "Barlow Condensed", sans-serif;
    text-transform: uppercase;
  }
  .line {
    position: absolute;
    left: 0;
    width: 100%;
    text-align: center;
    line-height: 1;
    white-space: nowrap;
  }
  .author {
    top: 25px;
    font-family: "Barlow Semi Condensed", sans-serif;
    font-weight: 700;
    font-size: 42px;
    letter-spacing: 0.3em;
    padding-left: 0.3em;
    color: var(--white);
  }
  .title-top {
    top: 67px;
    font-weight: 700;
    font-size: 160px;
    color: var(--accent);
  }
  .title-main {
    top: 192px;
    font-weight: 700;
    font-size: 223px;
    letter-spacing: -0.01em;
    color: var(--accent);
  }
  .subtitle {
    top: 413px;
    display: flex;
    align-items: center;
    justify-content: center;
    gap: 18px;
    font-weight: 700;
    font-size: 58px;
    color: var(--white);
  }
  .subtitle .rule {
    width: 69px;
    height: 4px;
    background: var(--accent);
  }
  .plate-art {
    position: absolute;
    left: 172px;
    top: 497px;
    width: 452px;
    height: 452px;
    border-radius: 50%;
    background: radial-gradient(circle at 50% 52%,
      var(--plate-well) 0%,
      var(--plate-light) 30%,
      var(--plate-mid) 52%,
      var(--plate-light) 70%,
      var(--plate-mid) 88%,
      var(--plate-rim) 100%);
    box-shadow: 0 18px 40px var(--plate-shadow);
  }
  .promise {
    top: 956px;
    font-weight: 700;
    font-size: 46px;
    color: var(--accent);
  }
  .promise-white {
    top: 1002px;
    font-weight: 700;
    font-size: 44px;
    color: var(--white);
  }
  .promise-small {
    top: 1047px;
    font-weight: 700;
    font-size: 36px;
    color: var(--accent);
  }
</style>
</head>
<body>
  <main class="cover">
    <p class="line author">Colin Mayhew</p>
    <h1 class="line title-top">Folding</h1>
    <h1 class="line title-main">The Map</h1>
    <h2 class="line subtitle"><span class="rule"></span>Weight Loss Secrets<span class="rule"></span></h2>
    <div class="plate-art" role="img" aria-label="Illustration of a plate seen from above with a fork, spoon, magnifying glass over a slice of bread and tomato slices"></div>
    <p class="line promise">For losing all the weight you want</p>
    <p class="line promise-white">&amp; keeping it off forever</p>
    <p class="line promise-small">No matter what you have tried in the past</p>
  </main>
</body>
</html>
```